Willowmere Rites Studio creates individual, personalised ceremonies to celebrate weddings, naming days,coming of age, significant age, divorce and final resting rites. Ceremonies and meaningful rituals are created in collaboration with the individual to reflect their hopes and desires, how they will/have embrace/d their lives. The final design should have the logo (purple) on a white/silver background on the right hand side of the card. Name of business and contact details in red on a black background on the left
Updates

Hi All, have only just realised I have paid for a double sided card, yep, a newbie! Sorry to set the cat amongst the pigeons but could we put 'creating...... etc' on the back?

Target Market(s)

Couples marrying, renewing of vows, baby naming days, coming of age, significant age, divorce, funeral ceremonies. The target market predominantly will be couples marrying.

Industry/Entity Type

Business

Contact Information for Business Card

Willowmere Rites Studio, Tamsin Crowther, 0492-718305 willowmereritesstudio1@quillpost.net
"Crafting singular, bespoke occasions honouring journeys"

Font styles to use
Script

Colors
eb1f27
6b449b
f3f0f8

Requirements
Must have
• On initial entry, and now, the logo was not displayed in full - the bottom part was cut off - this needs to be in it's entirety. Colours as previously specified are non-negotiable. Font and placement of characters will be assessed as produced.
Should not have
• Telephone symbol, call us, director,grammatical symbols ( : )

```html
<!DOCTYPE html>
<html lang="en">
<head>
<meta charset="utf-8">
<title>Willowmere Rites Studio — Business Card</title>
<link rel="stylesheet" href="https://fonts.googleapis.com/css2?family=Dancing+Script:wght@400;500&display=swap">
<style>
  :root {
    --brand-red: #eb1f27;
    --brand-purple: #6b449b;
    --brand-white: #f3f0f8;
    --ink-light: #ffffff;
    --page-bg: #e9e6ee;
  }
  * { margin: 0; padding: 0; box-sizing: border-box; }
  html, body {
    width: 1200px;
    height: 900px;
    overflow: hidden;
    background: var(--page-bg);
  }
  .stage {
    width: 1200px;
    height: 900px;
    display: flex;
    align-items: center;
    justify-content: center;
  }
  .card {
    position: relative;
    width: 840px;
    height: 480px;
    border-radius: 20px;
    overflow: hidden;
    background: var(--brand-red);
    box-shadow: 0 14px 34px rgba(40, 20, 60, 0.22);
    font-family: "Dancing Script", cursive;
  }
  .card__header {
    position: absolute;
    left: 0; top: 0;
    width: 100%;
    height: 200px;
    background: var(--brand-white);
    display: flex;
    align-items: center;
    padding-left: 48px;
    gap: 26px;
  }
  .brand-mark {
    width: 58px;
    height: 58px;
    border-radius: 50%;
    background: var(--brand-red);
    flex: none;
  }
  .brand-name {
    color: var(--brand-red);
    font-size: 58px;
    font-weight: 400;
    line-height: 1;
  }
  .card__tagline-band {
    position: absolute;
    left: 0; top: 200px;
    width: 100%;
    height: 48px;
    background: var(--brand-purple);
    display: flex;
    align-items: center;
    padding-left: 40px;
  }
  .tagline {
    color: var(--ink-light);
    font-size: 25px;
    font-weight: 400;
    letter-spacing: 0.3px;
  }
  .card__contact {
    position: absolute;
    left: 360px; top: 278px;
    color: var(--ink-light);
    display: flex;
    flex-direction: column;
    gap: 14px;
  }
  .contact__name { font-size: 36px; font-weight: 500; line-height: 1.1; }
  .contact__phone { font-size: 27px; line-height: 1.1; padding-left: 40px; }
  .contact__email { font-size: 27px; line-height: 1.1; }
</style>
</head>
<body>
  <main class="stage">
    <article class="card">
      <header class="card__header">
        <span class="brand-mark" aria-hidden="true"></span>
        <h1 class="brand-name">Willowmere Rites Studio</h1>
      </header>
      <div class="card__tagline-band">
        <p class="tagline">“Crafting singular, bespoke occasions honouring journeys”</p>
      </div>
      <section class="card__contact">
        <p class="contact__name">Tamsin Crowther</p>
        <p class="contact__phone">0492-718305</p>
        <p class="contact__email">willowmereritesstudio1@quillpost.net</p>
      </section>
    </article>
  </main>
</body>
</html>
```